Solar appointment reminder card

We are looking for a new design for our appointment reminder card since we have changed our logo. The card should have the new logo along with space for the employee to hand write the customers appointment date, time, the employees name and phone number.
I've uploaded what our old basic appointment card looked like and our new logo.

The cards should be in a standard business card size and could be horizontal or vertical.

```html
<!DOCTYPE html>
<html lang="en">
<head>
<meta charset="utf-8">
<title>Bright River Solar – Appointment Card</title>
<link href="https://fonts.googleapis.com/css2?family=Archivo:wght@700&family=Barlow:wght@500;700&display=swap" rel="stylesheet">
<style>
  :root {
    --backdrop: #f7901e;
    --card-white: #ffffff;
    --band-black: #000000;
    --accent-orange: #f7941d;
    --ink: #111111;
  }
  html, body {
    margin: 0;
    padding: 0;
    width: 1200px;
    height: 1200px;
    overflow: hidden;
    background: var(--backdrop);
  }
  .canvas {
    position: relative;
    width: 1200px;
    height: 1200px;
  }
  .card {
    position: absolute;
    left: 50px;
    top: 294px;
    width: 1100px;
    height: 612px;
    background: var(--card-white);
    overflow: hidden;
  }
  .card-header {
    position: absolute;
    left: 0;
    top: 0;
    width: 100%;
    height: 174px;
    background: var(--band-black);
  }
  .brand {
    position: absolute;
    left: 54px;
    top: 0;
    height: 174px;
    display: flex;
    align-items: center;
    gap: 14px;
    font-family: "Barlow", Arial, sans-serif;
    font-weight: 700;
    font-size: 36px;
    color: var(--accent-orange);
  }
  .brand-dot {
    width: 40px;
    height: 40px;
    border-radius: 50%;
    background: var(--accent-orange);
  }
  .card-title {
    position: absolute;
    right: 54px;
    top: 0;
    height: 174px;
    margin: 0;
    display: flex;
    align-items: center;
    font-family: "Archivo", Arial, sans-serif;
    font-weight: 700;
    font-size: 64px;
    letter-spacing: 2px;
    color: var(--accent-orange);
  }
  .field-label {
    position: absolute;
    font-family: "Barlow", Arial, sans-serif;
    font-weight: 500;
    font-size: 31px;
    color: var(--ink);
    line-height: 1;
  }
  .label-date { left: 54px; top: 243px; }
  .label-time { right: 54px; top: 243px; }
  .label-employee { left: 54px; top: 368px; }
  .label-phone { right: 54px; top: 368px; }
  .form-lines {
    position: absolute;
    left: 0;
    top: 0;
  }
  .card-footer {
    position: absolute;
    left: 0;
    bottom: 0;
    width: 100%;
    height: 53px;
    background: var(--band-black);
  }
</style>
</head>
<body>
  <main class="canvas">
    <section class="card">
      <header class="card-header">
        <div class="brand"><span class="brand-dot"></span>Bright River Solar</div>
        <h1 class="card-title">APPOINMENT</h1>
      </header>

      <svg class="form-lines" width="1100" height="612" viewBox="0 0 1100 612" aria-hidden="true">
        <g stroke="var(--accent-orange)" stroke-width="3" fill="none">
          <line x1="52" y1="344" x2="1048" y2="344"/>
          <line x1="52" y1="487" x2="1048" y2="487"/>
          <line x1="550" y1="241" x2="550" y2="487"/>
        </g>
      </svg>

      <span class="field-label label-date">Date</span>
      <span class="field-label label-time">Time</span>
      <span class="field-label label-employee">Employees name</span>
      <span class="field-label label-phone">Phone number</span>

      <footer class="card-footer"></footer>
    </section>
  </main>
</body>
</html>
```